Flyer-Design für Prozessfinanzierungsfirma
Zielgruppe
Wir sind eine Prozessfinanzierungsfirma. im Versicherungsbereich die größte Österreichs mit mehr als 50.000 Klienten und unser neues Projekt ist die Prozessfinanzierung von Patienten die durch einen Kunstfehler (Fehler von Ärzten) auf Schadenersatz klagen wollen aber nicht die Finanziellen Möglichkeiten haben.
Aufgabenstellung
Folder soll eine DIN A4 Doppelseite sein (also 4 A4 Seiten)
plus extra ein A4 Einlage Blatt Fragebogen fix vorgegebene Fragen.
#258971 Dieser Folder ist für die gleiche Firma im Bereich Versicherungen
www.heilirrtum-hilfe.at. TEXTE und DESIGN - FARBEN und INHALTE von dieser Homepage übernehmen
die Seite www.policenportal.at ist die gleiche Prozessfinanzierungsfirma - hier gibt es bereits einen Folder. Ich lade diesen hoch...
Diese Fragen sind unbedingt 1:1 zu übernehmen für das Einlageblatt :
o Was waren meine Erkrankungen vor der Behandlung, inkl. Dauermedikation?
o Warum ging ich zum Arzt?
o Was hat mir der Arzt empfohlen?
o Wurde ich über die unterschiedlichen Behandlungsmöglichkeiten aufgeklärt?
o Was wollte ich haben?
o Was wurde gemacht?
o Was hat der Arzt aus meiner Sicht falsch gemacht?
o Was wurde als weiterer Behandlungsweg empfohlen?
o Habe ich den Arzt mit meinem Problem konfrontiert?
o Wie hat mein Arzt darauf reagiert?
o Was ist jetzt genau schlechter als vorher?
Bei dem A4 Einlageblatt sollen auf der Vorderseite und der halben Rückseite diese Fragen mit entsprechendem Platz für den Text zum ausfüllen erscheinen und die untere Hälfte der 2. Seite mit einem kurzen Slogan nochmal auf unsere Leistung aufmerksam machen - ein Feld in Kreditkartengrösse für den Empfehlungsbgeber weiss zum einkleben einer Karte freibleiben und die Firmendaten (siehe Homepage) mit Anschrift, Telefonnummer und e-mailadresse angegeben sein

```html
<!DOCTYPE html>
<html lang="de">
<head>
<meta charset="utf-8">
<title>Folder Kunstfehler – Innenseiten</title>
<link href="https://fonts.googleapis.com/css2?family=Crimson+Text:wght@400;600;700&display=swap" rel="stylesheet">
<style>
  :root{
    --backdrop:#3b2e2c;
    --paper:#fbfbfa;
    --ink:#1f1c1b;
    --sand:#c9bdae;
    --mauve:rgba(150,110,105,.30);
    --mauve-light:rgba(175,140,132,.22);
    --burgundy:#7a2a30;
    --photo-top-a:#f1f1f2;
    --photo-top-b:#7d6f68;
    --photo-bottom-a:#3c4148;
    --photo-bottom-b:#c9a987;
  }
  *{box-sizing:border-box;margin:0;padding:0}
  html,body{width:1200px;height:867px;overflow:hidden;background:var(--backdrop)}
  ul{list-style:none}
  .spread{
    position:absolute;left:40px;top:37px;width:1120px;height:792px;
    background:var(--paper);overflow:hidden;
    font-family:"Crimson Text",Georgia,serif;color:var(--ink);
    box-shadow:0 10px 30px rgba(0,0,0,.45);
  }
  .photo{position:absolute}
  .photo--team{
    left:130px;top:0;width:990px;height:300px;
    background:linear-gradient(100deg,var(--photo-top-a) 0%,#d9d4d0 35%,var(--photo-top-b) 60%,#e4e2e2 85%,var(--photo-top-a) 100%);
  }
  .photo--handshake{
    left:560px;top:612px;width:560px;height:180px;
    background:linear-gradient(160deg,var(--photo-bottom-a) 0%,#5a5f68 40%,var(--photo-bottom-b) 75%,#9eb0c6 100%);
  }
  .decor{position:absolute;inset:0;width:1120px;height:792px}
  .gutter{position:absolute;left:559px;top:0;width:2px;height:792px;background:linear-gradient(90deg,rgba(0,0,0,.08),rgba(0,0,0,.18),rgba(0,0,0,.08))}
  .accent-band{position:absolute;left:1000px;top:292px;width:120px;height:40px;background:var(--burgundy)}
  .block{position:absolute;font-size:11.2px;line-height:1.32}
  .block h2{font-size:13.5px;font-weight:700;margin:0 0 4px}
  .block p{margin:0 0 8px;text-align:justify;hyphens:auto}
  .block li{position:relative;padding-left:10px;margin-bottom:6px;text-align:justify;hyphens:auto}
  .block li::before{content:"•";position:absolute;left:0;top:0}
  .intro{left:44px;top:112px;width:300px}
  .claims-lead{left:44px;top:354px;width:480px;font-weight:700;font-size:12px}
  .claims-a{left:44px;top:376px;width:228px}
  .claims-b{left:292px;top:376px;width:232px;font-size:10.6px}
  .difficulty{left:594px;top:312px;width:284px;font-size:10.8px;line-height:1.28}
  .difficulty p{margin-bottom:6px}
  .offer{left:898px;top:340px;width:205px;font-size:10.8px}
  .offer h2{font-size:14px}
  .offer li{text-align:left;margin-bottom:5px}
</style>
</head>
<body>
<main class="spread">
  <div class="photo photo--team" role="img" aria-label="Foto: Ärzteteam betrachtet gemeinsam ein Röntgenbild"></div>
  <div class="photo photo--handshake" role="img" aria-label="Foto: Handschlag über einem unterzeichneten Vertrag"></div>

  <svg class="decor" viewBox="0 0 1120 792" aria-hidden="true">
    <polygon points="0,90 560,90 560,345 0,345" fill="var(--sand)" opacity=".92"/>
    <polygon points="560,300 1120,300 1120,612 560,612" fill="var(--paper)"/>
    <polygon points="470,792 560,640 640,250 700,250 600,792" fill="var(--mauve)"/>
    <polygon points="560,240 760,240 620,300 560,330" fill="var(--mauve-light)"/>
    <polygon points="380,792 560,560 560,640 460,792" fill="var(--mauve-light)"/>
  </svg>
  <div class="gutter"></div>
  <div class="accent-band"></div>

  <section class="block intro">
    <h2>Was ist ein ärztlicher Kunstfehler?</h2>
    <p>Dies ist eigentlich ein umgangssprachlicher Ausdruck. Juristisch spricht man von sogenannten „Behandlungsfehlern“. Diese liegen vor, wenn eine medizinische Behandlung nicht nach den zum Zeitpunkt der Behandlung bestehenden, allgemein anerkannten fachlichen Standards erfolgt.</p>
    <p>Es ist egal, ob dieser Fehler aus einem aktiven Tun (z.B. falsche Operation) oder einem bloßen Unterlassen (mangelnde Aufklärung über Risken) resultierte.</p>
    <h2>Was kann der verletzte Patient fordern?</h2>
    <p>Erleidet nun ein Patient durch ein pflichtwidriges Verhalten eines Arztes (Behandlungsfehler) einen Schaden (z.B. Schmerzen), so kann der Verletzte dafür einen Geldbetrag fordern.</p>
  </section>

  <div class="block claims-lead">Man kann diese Forderungen wie folgt einteilen:</div>
  <ul class="block claims-a">
    <li>Schmerzengeld für erlittene Schmerzen. Diese werden gemäß Judikatur in schwere, mittlere und leichte Schmerzen eingeteilt. Multipliziert mit der Dauer dieser Schmerzen ergibt sich der Schmerzengeldanspruch.</li>
    <li>In letzter Zeit kann in Ausnahmefällen auch ein Anspruch für erlittene seelische Schmerzen zuerkannt werden (z.B.: Trauerschmerzengeld oder Schockschadenansprüche).</li>
    <li>Sind nach dem Ende der Schmerzperiode weitere Behandlungen notwendig, sind auch diese Kosten zu ersetzen (physikalische Therapien, Kuraufenthalte, Massagen, Medikamente, Fahrtkosten).</li>
    <li>Ist bis zur Genesung eine Heimhilfe oder eine weitere Betreuung notwendig, sind auch diese Kosten zu ersetzen.</li>
  </ul>
  <ul class="block claims-b">
    <li>Sollte der Umbau der Wohnung notwendig sein (der Patient ist nach dem Behandlungsfehler querschnittsgelähmt), sind auch die Umbaukosten der Wohnung zu ersetzen.</li>
    <li>Bleibt eine bleibende störende Narbe, kann dem Patienten eine Verunstaltungsentschädigung zugesprochen werden.</li>
    <li>Schließlich trifft den Arzt bzw. das Spital auch eine Haftung für alle weiteren Folgeschäden.</li>
  </ul>

  <section class="block difficulty">
    <h2>Warum ist eine Anspruchsverfolgung in der Praxis so schwierig?</h2>
    <p>Die Antwort liegt auf der Hand. Der „kleine Patient“ steht meist einem ganzen Spital oder einem erfahrenen Arzt gegenüber. Das Spital aber auch der behandelnde Arzt ist immer anwaltlich gut vertreten, eine Schuld wird fast immer abgestritten. Rechtsschutzversicherungen sind meist nicht vorhanden oder lehnen eine Deckung ab.</p>
    <p>Das Spital oder der behandelnde Arzt spielen außerdem oft auf Zeit und die drohende Verjährung (3 Jahre) sitzt den Patienten im Nacken.</p>
    <p>Dem verletzten Patienten bleibt sodann nur mehr die Möglichkeit, selbst den Gerichtsweg zu beschreiten, dies ist jedoch mit einem enormen Kostenrisiko verbunden.</p>
    <p>Da die Streitwerte oft hoch sind, besteht ein enormes Prozesskostenrisiko und man ist abhängig von medizinischen Gutachten, deren Ausgang meist nicht vorhersehbar ist.</p>
  </section>

  <section class="block offer">
    <h2>Doch damit ist nun Schluss!</h2>
    <p>Wir helfen Ihnen in dieser Situation schnell und unbürokratisch weiter. Wir übernehmen sämtliche anfallenden Kosten:</p>
    <ul>
      <li>Anwaltliches Erstgespräch und Folgegespräche</li>
      <li>Aufforderungsschreiben gegen die Versicherung</li>
      <li>Verhandlungen mit der Versicherung</li>
      <li>Klage gegen die Versicherung</li>
      <li>Kosten von Gutachten</li>
      <li>Kosten der Gerichtsverhandlungen</li>
      <li>Kosten von Berufungen und Revisionen</li>
    </ul>
  </section>
</main>
</body>
</html>
```